SKVC Stationary and business Card
SKVC letterhead and Business Card
Professional
Summit Kinship Vitality Center
Dr. Marcus Pellham, D.C. Dr. Tamsin Pellham, D.C.
2948 Arden Avenue Boulder, CO 80304
drpellham@summitvitalityclinics.com
www.summitvitalityclinics.com

```html
<!DOCTYPE html>
<html lang="en">
<head>
<meta charset="utf-8">
<title>SKVC Business Card</title>
<link href="https://fonts.googleapis.com/css2?family=Source+Sans+3:wght@400;600;700&display=swap" rel="stylesheet">
<style>
  :root {
    --page-bg: #e9e8ec;
    --card-white: #ffffff;
    --purple-light: #8a5aa8;
    --purple-deep: #5b2c7e;
    --swoosh-grey: #b9b6bd;
    --ink-dark: #2b2233;
    --text-light: #ffffff;
    --text-soft: #efe6f5;
    --spine-tint: rgba(255,255,255,0.14);
  }
  * { box-sizing: border-box; margin: 0; padding: 0; }
  html, body {
    width: 1200px; height: 780px; overflow: hidden;
    background: var(--page-bg);
    font-family: "Source Sans 3", "Helvetica Neue", Arial, sans-serif;
  }
  .canvas {
    position: relative; width: 1200px; height: 780px;
    display: flex; align-items: center; justify-content: center;
  }
  .business-card {
    position: relative; width: 1000px; height: 600px;
    border-radius: 34px; overflow: hidden;
    background: var(--card-white);
    box-shadow: 0 14px 36px rgba(40, 20, 60, 0.22);
  }
  .card-shapes { position: absolute; inset: 0; width: 100%; height: 100%; }
  .practitioner-name {
    position: absolute; right: 60px; top: 72px;
    font-size: 31px; font-weight: 700; color: var(--ink-dark);
  }
  .clinic-name {
    position: absolute; left: 70px; top: 262px;
    color: var(--text-light); font-weight: 600; line-height: 1;
  }
  .clinic-name .line-main { display: block; font-size: 54px; letter-spacing: 1px; }
  .clinic-name .line-sub { display: block; font-size: 26px; letter-spacing: 11px; margin-top: 8px; }
  .spine-area {
    position: absolute; right: 92px; top: 238px;
    width: 96px; height: 250px; border-radius: 48px;
    background: linear-gradient(180deg, var(--spine-tint), rgba(255,255,255,0.04));
  }
  .contact-block {
    position: absolute; left: 70px; top: 404px;
    color: var(--text-soft); font-size: 21px; font-weight: 400; font-style: normal;
  }
  .address { margin-bottom: 12px; }
  .contact-row { display: flex; align-items: center; gap: 10px; height: 31px; }
  .contact-row .gap { width: 22px; }
  .icon { width: 22px; height: 22px; flex: none; }
</style>
</head>
<body>
<main class="canvas">
  <section class="business-card">
    <svg class="card-shapes" viewBox="0 0 1000 600" preserveAspectRatio="none" aria-hidden="true">
      <defs>
        <linearGradient id="purpleFill" x1="0" y1="0" x2="1" y2="1">
          <stop offset="0" stop-color="var(--purple-light)"/>
          <stop offset="1" stop-color="var(--purple-deep)"/>
        </linearGradient>
      </defs>
      <path d="M0,208 C230,120 500,232 740,178 C860,150 940,120 1000,112 L1000,600 L0,600 Z" fill="var(--swoosh-grey)"/>
      <path d="M0,234 C250,150 520,258 760,202 C870,176 940,150 1000,146 L1000,600 L0,600 Z" fill="url(#purpleFill)"/>
    </svg>

    <p class="practitioner-name">Dr. Marcus Pellham, D.C.</p>

    <h1 class="clinic-name">
      <span class="line-main">SUMMIT KINSHIP</span>
      <span class="line-sub">VITALITY CENTER</span>
    </h1>

    <div class="spine-area" role="img" aria-label="Faint spine illustration decoration"></div>

    <address class="contact-block">
      <p class="address">2948 Arden Avenue Boulder, CO 80304</p>
      <p class="contact-row">
        <svg class="icon" viewBox="0 0 24 24"><circle cx="12" cy="12" r="12" fill="#fff"/><path d="M8 6l3 0 1 3-2 1.5a8 8 0 0 0 3.5 3.5L15 12l3 1v3c-6 1-11-4-10-10z" fill="var(--purple-deep)"/></svg>
        <span>303.555.0142</span>
        <span class="gap"></span>
        <svg class="icon" viewBox="0 0 24 24"><circle cx="12" cy="12" r="12" fill="#fff"/><rect x="7" y="10" width="10" height="7" rx="1" fill="var(--purple-deep)"/><rect x="8.5" y="6" width="7" height="4" fill="var(--purple-deep)"/></svg>
        <span>303.555.0147</span>
      </p>
      <p class="contact-row">
        <svg class="icon" viewBox="0 0 24 24"><circle cx="12" cy="12" r="12" fill="#fff"/><rect x="6" y="8" width="12" height="8" fill="var(--purple-deep)"/><path d="M6 8l6 5 6-5" stroke="#fff" stroke-width="1.3" fill="none"/></svg>
        <span>drpellham@summitvitalityclinics.com</span>
      </p>
      <p class="contact-row">
        <svg class="icon" viewBox="0 0 24 24"><circle cx="12" cy="12" r="12" fill="#fff"/><circle cx="12" cy="12" r="6" fill="none" stroke="var(--purple-deep)" stroke-width="1.5"/><path d="M6 12h12M12 6c-3 3-3 9 0 12M12 6c3 3 3 9 0 12" stroke="var(--purple-deep)" stroke-width="1.2" fill="none"/></svg>
        <span>www.summitvitalityclinics.com</span>
      </p>
    </address>
  </section>
</main>
</body>
</html>
```